Halvercott Orthodontics business card

Using our existing logo (created with ArtFolio), please create a tasteful, contemporary business card. We are father and daughter orthodontists specializing in braces, clarafit, etc to design healthy, beautiful smiles for children, adolescents, and adults. We would like the design to be family-friendly but not childish.
The final design should include all of the information without looking cluttered (I hope! If necessary to achieve an optimal design, please consider making the card double-sided)
Purple, black, silver on a white card
Please include the following information:
Halvercott Orthodontics (logo)
Marguerite L. Halvercott, DMD
Douglas R. Halvercott, DMD

312 Bramblewood Street
North Andover, MA 01899
978.555.0142

847C Quarry Hollow Street
Methuen, MA 01898
978.555.0187

email frontdesk@halvercottortho.example
website www.halvercottortho.example

```html
<!DOCTYPE html>
<html lang="en">
<head>
<meta charset="utf-8">
<title>Halvercott Orthodontics business card</title>
<link href="https://fonts.googleapis.com/css2?family=Libre+Baskerville:wght@400;700&display=swap" rel="stylesheet">
<style>
  :root {
    --purple: #4f2380;
    --purple-light: #5a2a8c;
    --purple-dark: #36104f;
    --ink: #555a60;
    --silver: #8a8d92;
    --paper: #ffffff;
    --backdrop: #ecebee;
  }
  * { box-sizing: border-box; margin: 0; padding: 0; }
  html, body {
    width: 1200px; height: 900px; overflow: hidden;
    background: var(--backdrop);
    font-family: "Libre Baskerville", Georgia, serif;
  }
  .canvas { position: relative; width: 1200px; height: 900px; }
  .card {
    position: absolute; left: 320px; width: 560px; height: 320px;
    border-radius: 30px;
    box-shadow: 0 10px 28px rgba(40, 20, 60, 0.18);
    overflow: hidden;
  }
  .card--front {
    top: 70px;
    background: radial-gradient(ellipse at 30% 85%, var(--purple-light) 0%, #48206f 50%, var(--purple-dark) 100%);
  }
  .card--back {
    top: 480px;
    background: linear-gradient(160deg, #ffffff 0%, #f6f5f8 60%, #ecebef 100%);
  }
  .brand {
    position: absolute; display: flex; align-items: center; gap: 12px;
    font-weight: 700; white-space: nowrap;
  }
  .brand__dot { width: 14px; height: 14px; border-radius: 50%; flex: none; }
  .card--front .brand { left: 120px; top: 190px; font-size: 25px; color: var(--paper); }
  .card--front .brand__dot { background: var(--paper); }
  .card--back .brand { right: 34px; top: 205px; font-size: 18px; color: var(--purple); }
  .card--back .brand__dot { background: var(--purple); width: 11px; height: 11px; }

  .doctors { position: absolute; left: 0; top: 42px; padding-left: 34px; }
  .doctors::before {
    content: ""; position: absolute; left: 0; top: 4px;
    width: 9px; height: 40px; background: var(--purple);
  }
  .doctor { font-size: 16px; font-weight: 700; color: var(--purple); line-height: 1.4; }
  .doctor__title { font-weight: 400; color: var(--silver); }

  .contacts { position: absolute; left: 34px; top: 112px; color: var(--ink); font-size: 13px; line-height: 1.45; }
  .office { margin-bottom: 14px; }
  .row { display: flex; align-items: flex-start; gap: 10px; }
  .icon { width: 13px; height: 13px; flex: none; margin-top: 3px; fill: var(--purple); }
  .row--indent { padding-left: 23px; }
  .online { position: absolute; left: 34px; bottom: 26px; color: var(--ink); font-size: 13px; line-height: 1.6; }
</style>
</head>
<body>
<main class="canvas">
  <section class="card card--front" aria-label="Card front">
    <div class="brand"><span class="brand__dot"></span>Halvercott Orthodontics</div>
  </section>

  <section class="card card--back" aria-label="Card back">
    <div class="doctors">
      <p class="doctor">Marguerite L. Halvercott<span class="doctor__title">, DMD</span></p>
      <p class="doctor">Douglas R. Halvercott<span class="doctor__title">, DMD</span></p>
    </div>

    <div class="contacts">
      <div class="office">
        <p class="row"><svg class="icon" viewBox="0 0 16 16"><path d="M3 1l3 3-1.5 2a9 9 0 0 0 5.5 5.5L12 10l3 3-2 2C7 15 1 9 1 3z"/></svg>978.555.0142</p>
        <p class="row"><svg class="icon" viewBox="0 0 16 16"><path d="M8 0a5.5 5.5 0 0 0-5.5 5.5C2.5 10 8 16 8 16s5.5-6 5.5-10.5A5.5 5.5 0 0 0 8 0zm0 8a2.5 2.5 0 1 1 0-5 2.5 2.5 0 0 1 0 5z"/></svg>312 Bramblewood Street</p>
        <p class="row row--indent">North Andover, MA 01899</p>
      </div>
      <div class="office">
        <p class="row"><svg class="icon" viewBox="0 0 16 16"><path d="M3 1l3 3-1.5 2a9 9 0 0 0 5.5 5.5L12 10l3 3-2 2C7 15 1 9 1 3z"/></svg>978.555.0187</p>
        <p class="row"><svg class="icon" viewBox="0 0 16 16"><path d="M8 0a5.5 5.5 0 0 0-5.5 5.5C2.5 10 8 16 8 16s5.5-6 5.5-10.5A5.5 5.5 0 0 0 8 0zm0 8a2.5 2.5 0 1 1 0-5 2.5 2.5 0 0 1 0 5z"/></svg>847C Quarry Hollow Street</p>
        <p class="row row--indent">Methuen, MA 01898</p>
      </div>
    </div>

    <div class="brand"><span class="brand__dot"></span>Halvercott Orthodontics</div>

    <div class="online">
      <p class="row"><svg class="icon" viewBox="0 0 16 16"><path d="M0 3h16v10H0z M1 4l7 5 7-5" stroke="#fff" stroke-width="1"/></svg>frontdesk@halvercottortho.example</p>
      <p class="row"><svg class="icon" viewBox="0 0 16 16"><circle cx="8" cy="8" r="7" fill="none" stroke="#4f2380" stroke-width="1.5"/><path d="M1 8h14M8 1c-3 4-3 10 0 14M8 1c3 4 3 10 0 14" fill="none" stroke="#4f2380" stroke-width="1.2"/></svg>www.halvercottortho.example</p>
    </div>
  </section>
</main>
</body>
</html>
```